Family Values Statement Image

I have created a statement of values for my family. Our last name is Tolvimar, and we are using those letters as an acronym. I would like an image with these words and letters with a tree with deep roots, where the roots are the focal point.

A - All In
N - Never Settle
D - Dependable
E - Enthusiastic
R - Repair
E - Enduring
G - Gushy Hearted
G - Gratitudes

Note that "gratitudes" is intentionally misspelled.

• On further reflection, I am interested in the words being much more prominent than the tree. In fact, the tree could be quite small or even just a watermark behind the words.

```html
<!DOCTYPE html>
<html lang="en">
<head>
<meta charset="utf-8">
<title>Tolvimar Family Values</title>
<link rel="stylesheet" href="https://fonts.googleapis.com/css2?family=Alegreya+SC:wght@800;900&family=Parisienne&family=Noto+Serif:wght@400;500&display=swap">
<style>
  :root {
    --paper: #ffffff;
    --gold-light: #f3c63c;
    --gold-mid: #dca423;
    --gold-deep: #b98410;
    --word-brown: #6c4d1b;
    --script-brown: #6a4a1a;
    --rule-gold: #dcc48c;
    --tree-tint: rgba(240, 224, 176, 0.55);
    --tree-fade: rgba(240, 224, 176, 0);
  }
  html, body {
    margin: 0;
    padding: 0;
    width: 800px;
    height: 1200px;
    overflow: hidden;
    background: var(--paper);
  }
  .poster {
    position: relative;
    width: 800px;
    height: 1200px;
    overflow: hidden;
    background: var(--paper);
  }
  .tree-watermark {
    position: absolute;
    left: 50px;
    top: 290px;
    width: 740px;
    height: 820px;
    background: radial-gradient(ellipse 50% 50% at 50% 48%, var(--tree-tint) 0%, rgba(240,224,176,0.3) 55%, var(--tree-fade) 100%);
  }
  .family-name {
    position: absolute;
    top: 112px;
    left: 0;
    width: 800px;
    margin: 0;
    text-align: center;
    font-family: "Alegreya SC", serif;
    font-weight: 900;
    font-size: 118px;
    line-height: 1;
    letter-spacing: -1px;
    background: linear-gradient(180deg, var(--gold-light) 0%, var(--gold-mid) 55%, var(--gold-deep) 100%);
    -webkit-background-clip: text;
    background-clip: text;
    color: transparent;
  }
  .subtitle {
    position: absolute;
    top: 232px;
    left: 0;
    width: 800px;
    display: flex;
    justify-content: center;
    align-items: center;
    gap: 24px;
  }
  .subtitle-rule {
    width: 56px;
    height: 1.5px;
    background: var(--rule-gold);
  }
  .subtitle-text {
    font-family: "Parisienne", cursive;
    font-size: 50px;
    line-height: 1;
    color: var(--script-brown);
  }
  .values {
    position: absolute;
    top: 314px;
    left: 106px;
    margin: 0;
    padding: 0;
    list-style: none;
  }
  .value {
    display: flex;
    align-items: baseline;
    height: 90.5px;
  }
  .value-initial {
    display: inline-block;
    width: 64px;
    text-align: center;
    font-family: "Alegreya SC", serif;
    font-weight: 800;
    font-size: 76px;
    line-height: 1;
    background: linear-gradient(180deg, var(--gold-light) 0%, var(--gold-mid) 55%, var(--gold-deep) 100%);
    -webkit-background-clip: text;
    background-clip: text;
    color: transparent;
  }
  .value-word {
    font-family: "Noto Serif", serif;
    font-weight: 400;
    font-size: 41px;
    line-height: 1;
    color: var(--word-brown);
    margin-left: 4px;
  }
</style>
</head>
<body>
  <main class="poster">
    <div class="tree-watermark" role="img" aria-label="Faint golden watermark of a broad tree with deep, spreading roots"></div>

    <h1 class="family-name">TOLVIMAR</h1>
    <div class="subtitle">
      <span class="subtitle-rule"></span>
      <span class="subtitle-text">Family Values</span>
      <span class="subtitle-rule"></span>
    </div>

    <ul class="values">
      <li class="value"><span class="value-initial">A</span><span class="value-word">– All In</span></li>
      <li class="value"><span class="value-initial">N</span><span class="value-word">– Never Settle</span></li>
      <li class="value"><span class="value-initial">D</span><span class="value-word">– Dependable</span></li>
      <li class="value"><span class="value-initial">E</span><span class="value-word">– Enthusiastic</span></li>
      <li class="value"><span class="value-initial">R</span><span class="value-word">– Repair</span></li>
      <li class="value"><span class="value-initial">E</span><span class="value-word">– Enduring</span></li>
      <li class="value"><span class="value-initial">G</span><span class="value-word">– Gushy Hearted</span></li>
      <li class="value"><span class="value-initial">G</span><span class="value-word">– Gratitudes</span></li>
    </ul>
  </main>
</body>
</html>
```